Kettlebrook Holdings, LLC. What we do is rehab homes for the purpose of flipping them and also have a rental portfolio as well.

We do not have a logo so that will need to be part of the design process

Would like, if possible to have a house or something with housing or remodeling incorporated in design.

Industry/Entity Type

Rental

Contact Information for Business Card

Dale Varnum
912 thistle Ct.
Harrowgate, il 60177
847-555-0143
Fax 630-555-0178

```html
<!DOCTYPE html>
<html lang="en">
<head>
<meta charset="utf-8">
<title>Kettlebrook Holdings – Business Card</title>
<link rel="stylesheet" href="https://fonts.googleapis.com/css2?family=Marcellus&display=swap">
<style>
  :root {
    --backdrop: #e4e6e5;
    --card-white: #ffffff;
    --card-fade: #ebebeb;
    --brand-blue: #134a86;
    --brand-blue-deep: #0f3d70;
    --stripe-grey: #8e9296;
    --ink-dark: #2b2e33;
    --ink-light: #dfe7f1;
  }
  * { box-sizing: border-box; margin: 0; padding: 0; }
  html, body {
    width: 1200px; height: 900px; overflow: hidden;
    background: var(--backdrop);
    font-family: "Marcellus", serif;
  }
  .canvas {
    width: 1200px; height: 900px;
    display: flex; align-items: center; justify-content: center;
  }
  .business-card {
    position: relative;
    width: 900px; height: 514px;
    background: linear-gradient(180deg, var(--card-white) 0%, var(--card-fade) 62%);
    box-shadow: 0 14px 30px rgba(0,0,0,0.28);
    overflow: hidden;
  }
  .brand {
    position: absolute; top: 90px; left: 0; right: 0;
    display: flex; align-items: center; justify-content: center; gap: 16px;
  }
  .brand-mark {
    width: 22px; height: 22px; background: var(--brand-blue);
  }
  .brand-name {
    font-size: 40px; font-weight: 400; letter-spacing: 4px; color: var(--ink-dark);
    text-transform: uppercase; line-height: 1;
  }
  .job-title {
    position: absolute; top: 290px; right: 62px;
    font-size: 13px; letter-spacing: 1.5px; text-transform: uppercase;
    color: var(--brand-blue);
  }
  .stripe-top {
    position: absolute; top: 315px; left: 0; right: 0; height: 12px;
    background: var(--stripe-grey);
  }
  .info-band {
    position: absolute; top: 327px; left: 0; right: 0; height: 112px;
    background: var(--brand-blue);
    color: var(--ink-light);
  }
  .stripe-bottom {
    position: absolute; top: 439px; left: 0; right: 0; height: 16px;
    background: var(--stripe-grey);
  }
  .phone-band {
    position: absolute; top: 455px; left: 0; right: 0; bottom: 0;
    background: var(--brand-blue-deep);
    color: var(--ink-light);
  }
  .person-name {
    position: absolute; left: 62px; top: 52px;
    font-family: "Marcellus", serif;
    font-size: 34px; font-weight: 400; line-height: 1;
    color: #eef3f9; letter-spacing: 0.5px;
  }
  .contact {
    position: absolute; display: flex; align-items: center; gap: 10px;
    font-size: 17px; letter-spacing: 1px; line-height: 1; white-space: nowrap;
  }
  .contact svg { width: 16px; height: 16px; fill: var(--ink-light); flex: none; }
  .contact-fax { left: 360px; top: 70px; }
  .contact-address { left: 560px; top: 70px; }
  .contact-phone { left: 62px; top: 17px; }
</style>
</head>
<body>
<main class="canvas">
  <article class="business-card">
    <header class="brand">
      <span class="brand-mark"></span>
      <span class="brand-name">Kettlebrook Holdings</span>
    </header>

    <p class="job-title">General Manager</p>
    <div class="stripe-top"></div>

    <section class="info-band">
      <h1 class="person-name">Dale Varnum</h1>
      <p class="contact contact-fax">
        <svg viewBox="0 0 16 16" aria-hidden="true"><rect x="4" y="1" width="8" height="5"/><rect x="1" y="6" width="14" height="6" rx="1"/><rect x="4" y="10" width="8" height="5" fill="#134a86" stroke="#dfe7f1" stroke-width="1.2"/></svg>
        630-555-0178
      </p>
      <p class="contact contact-address">
        <svg viewBox="0 0 16 16" aria-hidden="true"><path d="M8 0C4.7 0 2.5 2.4 2.5 5.3 2.5 9.2 8 16 8 16s5.5-6.8 5.5-10.7C13.5 2.4 11.3 0 8 0zm0 7.6a2.3 2.3 0 1 1 0-4.6 2.3 2.3 0 0 1 0 4.6z"/></svg>
        912 thistle Ct. Harrowgate, il 60177
      </p>
    </section>

    <div class="stripe-bottom"></div>

    <footer class="phone-band">
      <p class="contact contact-phone">
        <svg viewBox="0 0 16 16" aria-hidden="true"><path d="M3.6 1l2.3 3-1.3 1.8c.9 2 2.6 3.7 4.6 4.6l1.8-1.3 3 2.3-1.4 2.6C7 13.8 2.2 9 1 3l2.6-2z"/></svg>
        847-555-0143
      </p>
    </footer>
  </article>
</main>
</body>
</html>
```